Website design improvement for existing site

We would like design ideas for how the inner pages (not the homepage) of www.talbrookpictures.com could be improved. We don't want to totally redesign the website. We want to improve / enhance / develop it further to look high-end, sophisticated and visually stunning.

Target Market(s)

High end video production clients. National and international TV networks and brands wanting commercial filming.

Industry/Entity Type

Videography

Other font styles liked:
• Existing site fonts

Requirements
Must have
• Improvement on the existing inner pages without totally re-working the design. We want to achieve a high-end sophisticated look with the existing branding (colours, images etc)
Nice to have
• Any ideas for improving the homepage are also welcome but we are mostly happy with this page so it is not the priority.
Should not have
• Any major changes to colours, styles etc.

```html
<!DOCTYPE html>
<html lang="en">
<head>
<meta charset="utf-8">
<title>About Me – Talbrook Pictures</title>
<link href="https://fonts.googleapis.com/css2?family=Josefin+Sans:ital,wght@0,400;0,600;1,400;1,600&family=Lato:wght@400;700&display=swap" rel="stylesheet">
<style>
:root{
  --ink:#222226;
  --dark:#3a3a40;
  --darker:#2f2f35;
  --accent:#f0a030;
  --brand-red:#d8262a;
  --mist:#f0f0f5;
  --muted:#8a8a90;
  --line:#e4e4ea;
  --white:#ffffff;
}
*{margin:0;padding:0;box-sizing:border-box}
html,body{width:1200px;height:3249px;overflow:hidden}
body{position:relative;background:var(--white);font-family:"Lato",sans-serif;color:var(--ink)}
.abs{position:absolute}
.display{font-family:"Josefin Sans",sans-serif;font-weight:400}

/* header */
.site-header{left:0;top:0;width:1200px;height:113px;background:var(--dark)}
.brand{left:46px;top:36px;display:flex;align-items:center;gap:10px;white-space:nowrap}
.brand-dot{width:36px;height:36px;border-radius:50%;background:var(--brand-red);flex:none}
.brand-name{font-family:"Josefin Sans",sans-serif;font-weight:600;font-size:19px;color:var(--white);letter-spacing:.5px;text-transform:uppercase;line-height:36px;padding-top:4px}
.main-nav{left:352px;top:38px;display:flex;gap:40px;font-size:13px;letter-spacing:1.5px;text-transform:uppercase;color:#d8d8dc;white-space:nowrap}
.main-nav span{padding:10px 0}
.main-nav .current{color:var(--accent);border:2px solid var(--accent);padding:8px 14px;margin:0 -14px}
.social{left:986px;top:34px;display:flex;gap:26px}
.social span{width:40px;height:40px;border:2px solid #cfcfd4;border-radius:6px}

/* hero */
.hero{left:0;top:113px;width:1200px;height:294px;background:linear-gradient(100deg,#6b5a48 0%,#a88a62 35%,#8a6e52 65%,#5a4a3e 100%)}
.hero-shade{left:0;top:113px;width:1200px;height:294px;background:rgba(40,34,30,.25)}
.hero-title{left:0;top:190px;width:1200px;text-align:center;font-size:60px;color:var(--white)}
.crumbs{left:0;top:286px;width:1200px;text-align:center;font-size:15px;color:var(--white)}
.crumbs b{color:var(--accent);font-weight:400}

/* about */
.portrait-frame{left:43px;top:451px;width:447px;height:444px;background:var(--mist);padding:14px}
.portrait{width:100%;height:100%;background:linear-gradient(160deg,#f4f4f4 0%,#d9c6b4 45%,#8c7c70 100%)}
.about-lead{left:613px;top:448px;width:460px;font-size:28px;font-style:italic;font-weight:600;line-height:34px}
.about-rule{left:613px;top:578px;width:450px;height:1px;background:var(--line)}
.about-text{left:613px;top:608px;width:450px;font-size:12.5px;line-height:22px;color:var(--muted)}

/* videos */
.videos{left:0;top:964px;width:1200px;height:791px;background:var(--mist)}
.section-title{width:1200px;left:0;text-align:center;font-size:52px}
.section-sub{left:190px;width:820px;text-align:center;font-size:12px;line-height:24px;color:var(--muted)}
.tile{top:1274px;height:407px}
.tile-balloons{left:0;width:372px;background:linear-gradient(135deg,#d8452e 0%,#e8a070 45%,#3a3a34 100%)}
.tile-sunset{left:828px;width:372px;background:linear-gradient(180deg,#f2c24a 0%,#d29a3a 40%,#7a8a4a 75%,#4a5a34 100%)}
.tile-bride{left:372px;top:1245px;width:456px;height:466px;background:linear-gradient(160deg,#c9b8a6 0%,#a0887a 55%,#7a5e56 100%)}
.tile-veil{left:372px;top:1245px;width:456px;height:466px;background:rgba(80,66,60,.45);border:4px solid rgba(255,255,255,.25)}
.play{width:46px;height:46px}
.video-label{left:372px;top:1450px;width:456px;text-align:center;color:var(--white);font-family:"Josefin Sans",sans-serif;font-weight:600;font-size:24px}
.video-rule{left:570px;top:1505px;width:60px;height:2px;background:var(--white)}
.video-text{left:408px;top:1530px;width:384px;text-align:center;color:var(--white);font-size:13px;line-height:24px}
.arrow{width:20px;height:20px}

/* testimonials */
.feedback-link{left:0;top:1906px;width:1200px;text-align:center;font-size:12px;color:var(--muted)}
.feedback-link b{color:var(--accent);font-weight:400}
.quote-card{top:1965px;width:543px;height:281px;border:1px solid var(--line);border-bottom:none;background:var(--white)}
.quote-title{position:absolute;left:52px;top:45px;font-family:"Josefin Sans",sans-serif;font-weight:400;font-size:21px;white-space:nowrap}
.quote-mark{position:absolute;left:50px;top:100px;font-family:"Josefin Sans",sans-serif;font-size:56px;line-height:40px;color:#b8b8be}
.quote-body{position:absolute;left:100px;top:96px;width:400px;font-size:12px;line-height:24px;color:var(--muted)}
.quote-meta{position:absolute;left:52px;top:192px;display:flex;align-items:center;gap:26px;font-size:11px;color:var(--ink);text-transform:uppercase}
.avatar{width:40px;height:40px;border-radius:50%;background:linear-gradient(135deg,#c8a890,#7a5c4c)}
.quote-meta i{font-style:italic;color:var(--muted);text-transform:none;margin-left:30px}

/* booking */
.booking{left:0;top:2246px;width:1200px;height:682px;background:linear-gradient(180deg,#c9a67e 0%,#8e8a6e 40%,#6e705e 70%,#a8a29a 100%)}
.booking-shade{left:0;top:2246px;width:1200px;height:682px;background:linear-gradient(90deg,rgba(40,40,44,.35),rgba(40,40,44,.1))}
.booking-form{left:56px;top:2355px;width:568px;height:472px;border:2px solid rgba(255,255,255,.55)}
.field{left:160px;width:360px;height:34px;border-bottom:1px solid rgba(255,255,255,.5);color:var(--white);font-size:12px}
.book-btn{left:160px;top:2716px;width:360px;height:42px;border:2px solid var(--accent);color:var(--accent);font-size:12px;text-transform:uppercase;letter-spacing:1px;text-align:center;line-height:38px}
.book-title{left:690px;top:2462px;width:366px;text-align:center;font-size:52px;line-height:72px;color:var(--white)}
.book-rule{left:843px;top:2625px;width:60px;height:2px;background:var(--white)}
.book-text{left:710px;top:2656px;width:326px;text-align:center;color:var(--white);font-size:12px;line-height:22px}

/* footer */
.site-footer{left:0;top:2928px;width:1200px;height:321px;background:var(--dark)}
.newsletter{left:329px;top:3060px;width:542px;height:38px;border-bottom:1px solid #8a8a90;color:var(--white);font-size:13px;display:flex;justify-content:space-between;align-items:flex-start}
.newsletter b{font-size:12px;letter-spacing:1px;text-transform:uppercase}
.footer-social{left:524px;top:3132px;display:flex;gap:26px}
.footer-social span{width:40px;height:40px;border:2px solid #cfcfd4;border-radius:6px}
.copyright{left:0;top:3198px;width:1200px;text-align:center;color:#b8b8be;font-size:11px}
.copyright u{color:#d8d8dc}
.to-top{left:1120px;top:3184px;width:45px;height:44px}
</style>
</head>
<body>

<header class="abs site-header"></header>
<div class="abs brand"><span class="brand-dot"></span><span class="brand-name">Talbrook Pictures</span></div>
<nav class="abs main-nav">
  <span>Home</span><span class="current">About ⌄</span><span>Process ⌄</span><span>Brand Stories ⌄</span><span>Contact</span>
</nav>
<div class="abs social"><span></span><span></span><span></span></div>

<div class="abs hero" role="img" aria-label="Photo of a wedding couple kissing under falling confetti"></div>
<div class="abs hero-shade"></div>
<h1 class="abs hero-title display">About Me</h1>
<div class="abs crumbs"><b>Home</b> &nbsp;/ &nbsp;About Me</div>

<div class="abs portrait-frame"><div class="portrait" role="img" aria-label="Photo of a videographer in a hat holding a professional camcorder"></div></div>
<h2 class="abs about-lead display">I've been working as a<br>professional videographer all my<br>adult life.</h2>
<div class="abs about-rule"></div>
<p class="abs about-text">Lorem Ipsum is simply dummy text of the printing and typesetting industry. Lorem Ipsum has been the industry's standard dummy text ever since the 1500s, when an unknown printer took a galley of type and scrambled it to make a type specimen book. It has survived not only five centuries, but also the leap into electronic typesetting, remaining essentially unchanged. It was popularised in the 1960s with the release of Letraset sheets containing Lorem Ipsum passages, and more recently with desktop publishing software like Aldus PageMaker including versions of Lorem Ipsum.</p>

<section class="abs videos"></section>
<h2 class="abs section-title display" style="top:1040px">Our Best Videos</h2>
<p class="abs section-sub" style="top:1128px">In our portfolio, there are hundreds of successful videos and dozens of satisfied customers. All clients I've been working with were more than satisfied with my works. Check out the gallery to learn more about my skills and style.</p>

<div class="abs tile tile-balloons" role="img" aria-label="Video still of a smiling woman with colourful balloons"></div>
<div class="abs tile tile-sunset" role="img" aria-label="Video still of a sunset over green hills"></div>
<div class="abs tile-bride" role="img" aria-label="Video still of a bride holding red roses"></div>
<div class="abs tile-veil"></div>

<svg class="abs play" style="left:175px;top:1454px" viewBox="0 0 46 46"><circle cx="23" cy="23" r="20" fill="none" stroke="#fff" stroke-width="3"/><path d="M18 14 L32 23 L18 32 Z" fill="#fff"/></svg>
<svg class="abs play" style="left:577px;top:1385px" viewBox="0 0 46 46"><circle cx="23" cy="23" r="20" fill="none" stroke="#fff" stroke-width="3"/><path d="M18 14 L32 23 L18 32 Z" fill="#fff"/></svg>
<svg class="abs play" style="left:975px;top:1454px" viewBox="0 0 46 46"><circle cx="23" cy="23" r="20" fill="none" stroke="#fff" stroke-width="3"/><path d="M18 14 L32 23 L18 32 Z" fill="#fff"/></svg>
<div class="abs video-label">Video #1</div>
<div class="abs video-rule"></div>
<p class="abs video-text">If you are looking for high quality videography services, I will be glad to help you.</p>
<svg class="abs arrow" style="left:10px;top:1468px" viewBox="0 0 20 20"><path d="M13 3 L6 10 L13 17" fill="none" stroke="#fff" stroke-width="2.5"/></svg>
<svg class="abs arrow" style="left:1168px;top:1468px" viewBox="0 0 20 20"><path d="M7 3 L14 10 L7 17" fill="none" stroke="#fff" stroke-width="2.5"/></svg>

<h2 class="abs section-title display" style="top:1818px">What People Say</h2>
<p class="abs feedback-link">Need more feedback? <b>Click Here!</b></p>

<article class="abs quote-card" style="left:43px">
  <h3 class="quote-title">The Best Videographer I Know</h3>
  <span class="quote-mark">“</span>
  <p class="quote-body">I am writing to thank you again for your excellent work in producing our promotional videos. You are professional, courteous, polite, and easy to work with.</p>
  <div class="quote-meta"><span class="avatar" role="img" aria-label="Client portrait"></span><span>Rhea Calloway</span><i>Jul 20, 2017</i></div>
</article>
<article class="abs quote-card" style="left:617px">
  <h3 class="quote-title">You Make the Best Wedding Videos!</h3>
  <span class="quote-mark">“</span>
  <p class="quote-body">I knew that I wanted to have you produce our wedding video after doing a lot of research. After finally finding your website and watching your videos, you were the optimal choice.</p>
  <div class="quote-meta"><span class="avatar" role="img" aria-label="Client portrait"></span><span>June Marlow</span><i>Jul 20, 2017</i></div>
</article>

<section class="abs booking" role="img" aria-label="Photo of a videographer beside a camera on a tripod at a sunlit beach"></section>
<div class="abs booking-shade"></div>
<div class="abs booking-form"></div>
<div class="abs field" style="top:2418px">Event Date</div>
<div class="abs field" style="top:2481px">Your Name</div>
<div class="abs field" style="top:2544px">E-mail</div>
<div class="abs field" style="top:2609px;height:48px">Comment</div>
<div class="abs book-btn">Make an Appointment</div>
<h2 class="abs book-title display">Book Your Shooting</h2>
<div class="abs book-rule"></div>
<p class="abs book-text">To order a video shoot, please share as many details about your particular project as possible. I will be giving you my feedback immediately after I receive your message!</p>

<footer class="abs site-footer"></footer>
<div class="abs newsletter"><span>Your E-mail...</span><b>Subscribe</b></div>
<div class="abs footer-social"><span></span><span></span><span></span></div>
<p class="abs copyright">Talbrook Pictures © 2017. <u>Privacy Policy</u></p>
<svg class="abs to-top" viewBox="0 0 45 44"><rect width="45" height="44" fill="#f0a030"/><path d="M16 25 L22.5 18 L29 25" fill="none" stroke="#fff" stroke-width="2.5"/></svg>

</body>
</html>
```